Holistic Health Coach needs a catchy and creative flyer

I need an eye-catching and convincing DL sized flyer for my new health coaching business. I provide advice and regular coaching to people on health, fitness and lifestyle issues.

I want these flyers to create awareness of my business as well as providing some information about what I do and the services that I can provide. I also want the flyers to have a strong and clear call-to-action so they can contact me.

I have provided some photos myself to be used in the flyer if necessary. I have also provided my logo. My Business name is called "Our Vital Ledger" however I want to market myself as a " Qualified Holistic Health Coach".

Target Market(s)

Men and Women of all ages who are trying to improve their health and fitness

Industry/Entity Type

Health And Wellness

Font styles to use
Sans Serif

Requirements
Must have
• My Business is called "Our Vital Ledger" (as seen in attached logo) but I would like the main marketing message of the flyer to be focused as " Qualified Holistic Health Coach" .
• The Flyer should be DL size.
• Strong call to action
• Catchy and memorable design- as I am a new business I want this to capture people's attention.
• Please see attached document for page content.
Nice to have
• I have also included some recent pictures of myself to be incorporated in the flyer, if appropriate.

```html
<!DOCTYPE html>
<html lang="en">
<head>
<meta charset="utf-8">
<title>Our Vital Ledger – Qualified Holistic Health Coach</title>
<link href="https://fonts.googleapis.com/css2?family=Sorts+Mill+Goudy&family=Open+Sans:wght@400&family=Oswald:wght@400;500;600&family=Montserrat:wght@500&display=swap" rel="stylesheet">
<style>
  :root {
    --page-bg: #e9e9e6;
    --paper: #ffffff;
    --forest: #1d6a4c;
    --leaf: #3f8f5c;
    --lime: #8dc63f;
    --lime-soft: #c6e58a;
    --foliage-dark: #1e3d1c;
    --foliage-mid: #3d6b32;
    --foliage-light: #7fa66a;
    --ink-grey: #4a4a4a;
    --white: #ffffff;
  }
  * { box-sizing: border-box; margin: 0; padding: 0; }
  html, body { width: 1200px; height: 835px; overflow: hidden; }
  body { background: var(--page-bg); position: relative; }

  .flyer {
    position: absolute; left: 412px; top: 20px;
    width: 375px; height: 795px;
    background: var(--paper); overflow: hidden;
    box-shadow: 0 4px 16px rgba(0,0,0,.18);
  }

  .brand { position: absolute; top: 36px; left: 0; width: 100%; text-align: center; }
  .brand-mark {
    display: block; width: 48px; height: 48px; margin: 0 auto 8px;
    border-radius: 50%; background: var(--lime);
  }
  .brand-name {
    font-family: "Montserrat", sans-serif; font-weight: 500;
    font-size: 13px; letter-spacing: 1px; color: var(--ink-grey);
    text-transform: uppercase;
  }

  .headline {
    position: absolute; top: 136px; left: 0; width: 100%;
    text-align: center; font-family: "Sorts Mill Goudy", serif;
    font-weight: 400; font-size: 35px; line-height: 41px;
    color: var(--forest);
  }

  .services { position: absolute; top: 226px; left: 64px; list-style: none; }
  .services li {
    position: relative; padding-left: 28px; height: 32px;
    font-family: "Open Sans", sans-serif; font-size: 16.5px; color: var(--leaf);
  }
  .services svg { position: absolute; left: 0; top: 4px; }

  .coach-photo {
    position: absolute; left: 0; top: 350px; width: 100%; height: 445px;
    background:
      linear-gradient(180deg, var(--paper) 0%, rgba(255,255,255,0) 14%),
      radial-gradient(ellipse at 30% 60%, var(--foliage-light) 0%, rgba(127,166,106,0) 45%),
      linear-gradient(180deg, var(--foliage-mid) 10%, var(--foliage-dark) 70%, #2f3b44 100%);
  }

  .coach-credentials {
    position: absolute; left: 144px; top: 498px; width: 220px; height: 67px;
    background: rgba(141,198,63,.92); padding: 8px 12px;
    color: var(--white);
  }
  .coach-name { font-family: "Oswald", sans-serif; font-weight: 500; font-size: 15px; line-height: 19px; }
  .coach-credentials p {
    font-family: "Oswald", sans-serif; font-style: italic; font-size: 10.5px; line-height: 16px;
  }

  .call-to-action {
    position: absolute; left: 193px; top: 700px; width: 200px; height: 52px;
    border: 2px solid var(--white); border-right: none; border-radius: 26px 0 0 26px;
    padding: 5px 0 0 40px;
  }
  .call-to-action svg { position: absolute; left: -14px; top: 10px; }
  .cta-prompt { font-family: "Oswald", sans-serif; font-size: 13px; letter-spacing: .8px; color: var(--lime-soft); }
  .cta-phone { font-family: "Oswald", sans-serif; font-weight: 600; font-size: 19px; line-height: 22px; color: var(--white); }
</style>
</head>
<body>
  <article class="flyer">
    <header class="brand">
      <span class="brand-mark"></span>
      <span class="brand-name">Our Vital Ledger</span>
    </header>

    <h1 class="headline">Qualified Holistic<br>Health Coach</h1>

    <ul class="services">
      <li><svg width="22" height="20" viewBox="0 0 22 20"><path d="M2 11 L8 17 L20 2" fill="none" stroke="var(--lime)" stroke-width="2.6" stroke-linecap="round"/></svg>Nutritional Advice</li>
      <li><svg width="22" height="20" viewBox="0 0 22 20"><path d="M2 11 L8 17 L20 2" fill="none" stroke="var(--lime)" stroke-width="2.6" stroke-linecap="round"/></svg>Fitness Planning</li>
      <li><svg width="22" height="20" viewBox="0 0 22 20"><path d="M2 11 L8 17 L20 2" fill="none" stroke="var(--lime)" stroke-width="2.6" stroke-linecap="round"/></svg>Natural Health Management</li>
      <li><svg width="22" height="20" viewBox="0 0 22 20"><path d="M2 11 L8 17 L20 2" fill="none" stroke="var(--lime)" stroke-width="2.6" stroke-linecap="round"/></svg>Lifestyle Assessment</li>
    </ul>

    <div class="coach-photo" role="img" aria-label="Photo of the health coach standing at a white railing in front of green foliage"></div>

    <div class="coach-credentials">
      <div class="coach-name">Clara Hensley</div>
      <p>- BA in Sport and Exercise Management</p>
      <p>- M Pharmacy</p>
    </div>

    <div class="call-to-action">
      <svg width="28" height="28" viewBox="0 0 28 28">
        <circle cx="14" cy="14" r="13" fill="var(--white)"/>
        <path d="M10 7 c-2 1 -3 3 -2 6 c1 4 4 7 8 8 c2 0 3 -1 4 -2 l-3 -3 l-2 1 c-2 -1 -3 -2 -4 -4 l1 -2 z" fill="var(--foliage-dark)"/>
      </svg>
      <div class="cta-prompt">Get Started Now!</div>
      <div class="cta-phone">(02) 5550 1234</div>
    </div>
  </article>
</body>
</html>
```